Business Card for Lawyer

I'm looking for a business card for my new law firm, based in Ontario, Canada. I would prefer single sided. I am partial (but not limited) to white and blue color wise and like things understated. Also, if you can work in the red KT rating symbol from Penrowe-Calloway, that would be a plus.

Target Market(s)

Old people - so it should be easy to read.

Industry/Entity Type

Business

Contact Information for Business Card

See the specs in the word document below. Also, see the design for my website. The card should have a similar look to the site.

Requirements
Must have
• Everything listed in the business card specs. I don't mind having the address set off at the bottom of the card on its own line.
Should not have
• 1) Any sort of design that could also be used by a tattoo parlour or a tarot card reader, mystic etc.
• 2) There should not be any photographs of me (or anyone else).

```html
<!DOCTYPE html>
<html lang="en">
<head>
<meta charset="utf-8">
<title>Harrow's Law Firm – Business Card</title>
<link rel="stylesheet" href="https://fonts.googleapis.com/css2?family=Cinzel:wght@400;600;700&family=Libre+Baskerville:wght@400;700&display=swap">
<style>
  :root {
    --page-bg: #e6e7ea;
    --card-bg: #ffffff;
    --ink: #111111;
    --band-black: #0c0c0c;
    --name-blue: #3f6cb8;
    --tagline-blue: #7b95d0;
    --badge-grey: #e2e4e8;
  }
  * { box-sizing: border-box; margin: 0; padding: 0; }
  html, body { width: 1200px; height: 900px; overflow: hidden; }
  body { background: var(--page-bg); position: relative; font-family: "Libre Baskerville", Georgia, serif; color: var(--ink); }

  .business-card {
    position: absolute; left: 100px; top: 164px; width: 1000px; height: 572px;
    background: var(--card-bg); box-shadow: 0 6px 24px rgba(0,0,0,.18);
  }

  .firm-name {
    position: absolute; left: 0; right: 0; top: 48px; text-align: center;
    font-family: "Cinzel", "Times New Roman", serif; font-weight: 700;
    font-size: 64px; line-height: 70px; letter-spacing: 6px; color: var(--ink);
  }

  .services-band {
    position: absolute; left: 20px; right: 20px; top: 204px; height: 48px;
    background: var(--band-black); color: #fff;
    display: flex; align-items: center; justify-content: space-around;
    font-family: "Cinzel", "Times New Roman", serif; font-size: 27px; letter-spacing: 1px;
  }
  .services-band .divider { width: 3px; height: 34px; background: #fff; }

  .office-address {
    position: absolute; left: 0; right: 0; top: 268px; text-align: center;
    font-weight: 700; font-size: 22px;
  }

  .lawyer-name {
    position: absolute; left: 40px; top: 312px;
    font-family: "Cinzel", "Times New Roman", serif; font-weight: 600;
    font-size: 34px; letter-spacing: 2px; color: var(--name-blue);
  }
  .lawyer-credentials {
    position: absolute; left: 40px; top: 356px;
    font-weight: 700; font-size: 24px;
  }

  .rating-badge {
    position: absolute; left: 40px; top: 428px; width: 200px; height: 56px;
    background: var(--badge-grey); border-radius: 6px;
  }

  .contact-list {
    position: absolute; left: 556px; top: 330px; list-style: none;
    font-size: 24px; line-height: 34px;
  }
  .contact-list li { display: flex; align-items: center; gap: 14px; }
  .contact-list svg { width: 24px; height: 24px; fill: var(--name-blue); flex: none; }

  .tagline-band {
    position: absolute; left: 520px; right: 20px; bottom: 22px; height: 46px;
    background: var(--tagline-blue); color: #fff;
    display: flex; align-items: center; justify-content: center;
    font-family: "Cinzel", "Times New Roman", serif; font-size: 24px; letter-spacing: 1px;
  }
</style>
</head>
<body>
  <main class="business-card">
    <h1 class="firm-name">Harrow's<br>Law Firm</h1>

    <div class="services-band">
      <span>Barrister Solicitor</span><span class="divider"></span>
      <span>Notary Public</span><span class="divider"></span>
      <span>Litigation Counsel</span>
    </div>

    <p class="office-address">24 Merrick Street East, Ground Floor, Hamilton, ON L8N 2K4</p>

    <h2 class="lawyer-name">Daniel R. Harrow</h2>
    <p class="lawyer-credentials">B.A. &amp; J.D.</p>

    <div class="rating-badge" role="img" aria-label="Peer rating badge"></div>

    <ul class="contact-list">
      <li><svg viewBox="0 0 24 24" aria-hidden="true"><path d="M6.6 10.8a15.1 15.1 0 0 0 6.6 6.6l2.2-2.2c.3-.3.7-.4 1-.2 1.1.4 2.3.6 3.6.6.6 0 1 .4 1 1V20c0 .6-.4 1-1 1A17 17 0 0 1 3 4c0-.6.4-1 1-1h3.5c.6 0 1 .4 1 1 0 1.3.2 2.5.6 3.6.1.3 0 .7-.2 1z"/></svg>647-555-0142</li>
      <li><svg viewBox="0 0 24 24" aria-hidden="true"><path d="M6 2h12v6H6zM3 9h18a2 2 0 0 1 2 2v6h-4v5H5v-5H1v-6a2 2 0 0 1 2-2zm4 8v3h10v-3z"/></svg>647.555.0187</li>
      <li><svg viewBox="0 0 24 24" aria-hidden="true"><path d="M12 2a10 10 0 1 0 0 20 10 10 0 0 0 0-20zm7.9 9h-3.9a15 15 0 0 0-1.4-6.5A8 8 0 0 1 19.9 11zM12 4.1c1 1.4 1.9 3.9 2 6.9h-4c.1-3 1-5.5 2-6.9zM9.4 4.5A15 15 0 0 0 8 11H4.1a8 8 0 0 1 5.3-6.5zM4.1 13H8a15 15 0 0 0 1.4 6.5A8 8 0 0 1 4.1 13zm7.9 6.9c-1-1.4-1.9-3.9-2-6.9h4c-.1 3-1 5.5-2 6.9zm2.6-.4A15 15 0 0 0 16 13h3.9a8 8 0 0 1-5.3 6.5z"/></svg>www.harrowslaw.ca</li>
      <li><svg viewBox="0 0 24 24" aria-hidden="true"><path d="M2 5h20v14H2zm2 2v.5l8 5 8-5V7zm0 2.8V17h16V9.8l-8 5z"/></svg>daniel@harrowslaw.ca</li>
    </ul>

    <div class="tagline-band">Getting the Results That Matter</div>
  </main>
</body>
</html>
```